Business Card - Apex Wellness

Please use the logo / design elements and font to design a business card that is eye catching and informative. If using "Direct Primary Care" logo element, you don't have to spell it out in the text.

Dr. Brendan Halvik
Apex Wellness - Direct Primary Care
4817 Tillbrook Rd. Suite 305
Fort Smith, AR 72916
Phone: 479-555-0137
ApexWellnessAR.example

```html
<!DOCTYPE html>
<html lang="en">
<head>
<meta charset="utf-8">
<title>Apex Wellness – Business Card</title>
<link rel="stylesheet" href="https://fonts.googleapis.com/css2?family=Montserrat:wght@400;500;600;700&display=swap">
<style>
  :root {
    --backdrop: #1e1e1e;
    --card: #ffffff;
    --navy: #0d1838;
    --royal: #3a5dab;
    --sky: #3bb4e6;
    --ink: #2f2f33;
  }
  * { margin: 0; padding: 0; box-sizing: border-box; }
  html, body {
    width: 1200px;
    height: 1059px;
    overflow: hidden;
    background: var(--backdrop);
    font-family: "Montserrat", sans-serif;
  }
  .card {
    position: absolute;
    left: 191px;
    top: 296px;
    width: 818px;
    height: 467px;
    background: var(--card);
    border-radius: 20px;
    overflow: hidden;
  }
  .brand {
    position: absolute;
    left: 28px;
    top: 26px;
    width: 385px;
  }
  .brand-name {
    display: block;
    font-weight: 700;
    font-size: 52px;
    line-height: 58px;
    color: var(--navy);
    letter-spacing: -1px;
    white-space: nowrap;
  }
  .brand-tagline {
    display: flex;
    align-items: center;
    gap: 14px;
    margin-top: 6px;
    font-weight: 700;
    font-size: 17px;
    color: var(--navy);
    white-space: nowrap;
  }
  .brand-tagline::before,
  .brand-tagline::after {
    content: "";
    flex: 1;
    height: 2px;
    background: var(--navy);
  }
  .accent-bar {
    position: absolute;
    left: 0;
    top: 142px;
    width: 15px;
    height: 63px;
    background: var(--sky);
  }
  .person-name {
    position: absolute;
    left: 28px;
    top: 135px;
    font-weight: 700;
    font-size: 35px;
    color: var(--sky);
    white-space: nowrap;
  }
  .person-role {
    position: absolute;
    left: 28px;
    top: 181px;
    font-weight: 500;
    font-size: 21px;
    color: var(--ink);
  }
  .contact {
    position: absolute;
    left: 28px;
    top: 229px;
    list-style: none;
    font-weight: 500;
    font-size: 20px;
    color: var(--ink);
  }
  .contact li {
    display: flex;
    align-items: flex-start;
    line-height: 32px;
  }
  .contact .address { margin-bottom: 14px; }
  .contact .icon {
    width: 20px;
    height: 20px;
    margin: 6px 8px 0 0;
    flex: none;
    fill: var(--sky);
  }
  .brand-decoration {
    position: absolute;
    left: 405px;
    top: 29px;
    width: 413px;
    height: 409px;
    border-radius: 50%;
    background: radial-gradient(circle at 50% 50%, #e8f5fc 0%, #bfe4f6 55%, #c6d2ec 100%);
  }
</style>
</head>
<body>
  <main class="card">
    <header class="brand">
      <span class="brand-name">Apex Wellness</span>
      <span class="brand-tagline">Direct Primary Care</span>
    </header>

    <div class="accent-bar"></div>
    <h1 class="person-name">Dr. Brendan Halvik</h1>
    <p class="person-role">Founder / Physician</p>

    <ul class="contact">
      <li class="address">
        <svg class="icon" viewBox="0 0 20 20"><path d="M10 1a6.5 6.5 0 0 0-6.5 6.5C3.5 12.5 10 19 10 19s6.5-6.5 6.5-11.5A6.5 6.5 0 0 0 10 1zm0 9a2.5 2.5 0 1 1 0-5 2.5 2.5 0 0 1 0 5z"/></svg>
        <span>4817 Tillbrook Rd. Suite 305<br>Fort Smith, AR 72916</span>
      </li>
      <li>
        <svg class="icon" viewBox="0 0 20 20"><path d="M2 8c0-3 3.5-4.5 8-4.5S18 5 18 8v1.5h-4V8H6v1.5H2zM5 11h10l2 6H3z"/></svg>
        <span>479-555-0137</span>
      </li>
      <li>
        <svg class="icon" viewBox="0 0 20 20"><path d="M2 6h3v12H2zM7 2h8v4h3v12H7zm2 7h2v2H9zm4 0h2v2h-2zm-4 4h2v2H9zm4 0h2v2h-2z"/></svg>
        <span>479-555-0184</span>
      </li>
      <li>
        <svg class="icon" viewBox="0 0 20 20"><path d="M1 5h18v11H1zm2 1.5 7 5 7-5"/><path d="M3 6.5 10 11l7-4.5" fill="none" stroke="#fff" stroke-width="1.4"/></svg>
        <span>hello@apexwellnessar.example</span>
      </li>
      <li>
        <svg class="icon" viewBox="0 0 20 20"><circle cx="10" cy="10" r="8.5"/><path d="M5 6c2 0 3 1 2.5 3S9 11 8 13s1 3 1 4M12 3c0 2 2 2 3 3s-1 3 0 4 2 0 3 1" fill="none" stroke="#fff" stroke-width="1.3"/></svg>
        <span>ApexWellnessAR.example</span>
      </li>
    </ul>

    <div class="brand-decoration" role="img" aria-label="Large brand symbol area in sky blue and royal blue tones"></div>
  </main>
</body>
</html>
```